ZESTMUNCHY
Zestmunchy is a food van, serving high vibe delicious food to go. This business is dedicated to healthy delicious feel good food, beauty in service and a sustainable planet.

The van will operate in the south west of western Australia at music festivals events markets wherever people need great food to go!

I like the idea of vibrant green mixed with a yellow?? background with some rays like the sun through the background.
The font needs to say vibrant energetic
TO ME -vibrant energetic font has to appear to be on the move - perhaps with shading??

I like fusha if that works for font? but the colour has to say food too.

I would like a symbol on the card a simple V turned into a womans raised arms. This should be vibrant too.
Thank you
Blessings
Marisol

Target Market(s)

target lovers of healthy high vibe food. music festival goers. age 18- 50 feel. audiance conscious eaters of feel great food

Industry/Entity Type

Events

Contact Information for Business Card

ZESTMUNCHY
High Vibe Food
Van
Marisol -owner/opperator
0458170396
Face book symbol - ZESTMUNCHY

on the I would like a logo of a simple V turned into a womans arms up toward the sky flip side

My number and name again
Zestmunchy- feel great mobile food
Festivals, events, markets & WHEREVER GOOD FRESH FOOD TO GO IS ENJOYED

Requirements
Nice to have
• Moving energetic font
colour that says high vibe and healthy food

a logo that is a simple V turned into a woman's raised arms in gratitude

```html
<!DOCTYPE html>
<html lang="en">
<head>
<meta charset="utf-8">
<title>Zestmunchy – Business Card</title>
<link rel="stylesheet" href="https://fonts.googleapis.com/css2?family=Open+Sans:wght@600;700;800&display=swap">
<style>
  :root {
    --backdrop: #1f3d2c;
    --card-green: #0f7a3e;
    --card-deep: #116b35;
    --band-green: #1b6e30;
    --glow-yellow: #f7e600;
    --logo-yellow: #f7ee16;
    --ink-white: #ffffff;
    --icon-blue: #2c3f94;
  }
  html, body {
    margin: 0;
    padding: 0;
    width: 1200px;
    height: 846px;
    overflow: hidden;
    background: var(--backdrop);
    font-family: "Open Sans", Arial, sans-serif;
  }
  .canvas {
    position: relative;
    width: 1200px;
    height: 846px;
  }
  .card {
    position: absolute;
    width: 640px;
    height: 364px;
    border-radius: 28px;
    overflow: hidden;
    box-shadow: 0 10px 24px rgba(0,0,0,0.35);
  }

  /* Brand block: name with tagline right-aligned beneath */
  .brand-block {
    position: absolute;
    display: flex;
    flex-direction: column;
    align-items: flex-end;
  }
  .brand {
    color: var(--logo-yellow);
    font-weight: 800;
    letter-spacing: 1px;
    margin: 0;
    line-height: 1;
    display: flex;
    align-items: center;
  }
  .brand__dot {
    display: inline-block;
    background: var(--logo-yellow);
    border-radius: 50%;
  }
  .tagline {
    color: var(--ink-white);
    font-weight: 700;
    margin: 0;
    white-space: nowrap;
  }

  /* Front */
  .card--front {
    left: 50px;
    top: 40px;
    background:
      radial-gradient(circle at 48% 60%, var(--glow-yellow) 0%, #c9d80f 14%, #5fae28 34%, var(--card-green) 58%, var(--card-deep) 100%);
  }
  .card__band {
    position: absolute;
    left: 0; top: 0;
    width: 640px;
    height: 364px;
  }
  .card--front .brand-block { left: 40px; top: 40px; }
  .card--front .brand { font-size: 52px; gap: 10px; }
  .card--front .brand__dot { width: 18px; height: 18px; }
  .card--front .tagline { font-size: 19px; margin-top: 8px; margin-right: 24px; }

  .person {
    position: absolute;
    left: 78px;
    top: 150px;
    color: var(--ink-white);
  }
  .person__name {
    margin: 0;
    font-size: 20px;
    font-weight: 700;
    letter-spacing: 0.5px;
  }
  .person__role {
    margin: 2px 0 0;
    font-size: 14px;
    font-weight: 600;
  }
  .contact {
    position: absolute;
    left: 78px;
    top: 208px;
    color: var(--ink-white);
    font-size: 18px;
    font-weight: 600;
    letter-spacing: 1px;
  }
  .contact__row {
    display: flex;
    align-items: center;
    gap: 12px;
    height: 24px;
  }
  .contact__social {
    display: block;
    width: 16px;
    height: 16px;
    background: var(--icon-blue);
    border-radius: 2px;
  }
  .services {
    position: absolute;
    left: 88px;
    top: 266px;
    margin: 0;
    padding: 0;
    list-style: none;
    color: var(--ink-white);
    font-size: 14.5px;
    font-weight: 600;
    line-height: 19px;
  }
  .services li::before { content: "\2022\00a0"; }
  .services li:nth-child(2) { padding-left: 4px; }
  .services li:nth-child(3) { padding-left: 8px; }
  .services li:nth-child(4) { padding-left: 12px; }

  /* Back */
  .card--back {
    left: 505px;
    top: 440px;
    background: var(--card-deep);
  }
  .card--back .brand-block { left: 62px; top: 130px; }
  .card--back .brand { font-size: 68px; gap: 14px; }
  .card--back .brand__dot { width: 24px; height: 24px; }
  .card--back .tagline { font-size: 26px; margin-top: 14px; margin-right: 30px; }
</style>
</head>
<body>
<main class="canvas">

  <section class="card card--front" aria-label="Business card front">
    <svg class="card__band" viewBox="0 0 640 364" aria-hidden="true">
      <path d="M0 256 Q 320 236 640 262 L640 364 L0 364 Z" fill="var(--band-green)" opacity="0.85"/>
    </svg>
    <div class="brand-block">
      <h1 class="brand"><span class="brand__dot"></span>ZESTMUNCHY</h1>
      <p class="tagline">FRESH ZEST FOOD VAN</p>
    </div>
    <div class="person">
      <p class="person__name">MARISOL</p>
      <p class="person__role">OWNER</p>
    </div>
    <div class="contact">
      <div class="contact__row">
        <svg width="16" height="18" viewBox="0 0 16 18" aria-hidden="true">
          <rect x="0" y="0" width="16" height="18" rx="2" fill="#ffffff"/>
          <path d="M5 4 Q3 9 6 14 L8 13 L7 10 L5.5 9.5 Q5.5 7.5 6.5 6 L8 6 L8 3.5 Z" fill="#1b5e2e"/>
        </svg>
        <span>0458170396</span>
      </div>
      <div class="contact__row">
        <span class="contact__social" role="img" aria-label="Social page"></span>
      </div>
    </div>
    <ul class="services">
      <li>MOBILE FOOD FESTIVALS</li>
      <li>EVENTS</li>
      <li>MARKETS</li>
      <li>WHEREVER GOOD FRESH FOOD TO GO IS ENJOYED</li>
    </ul>
  </section>

  <section class="card card--back" aria-label="Business card back">
    <div class="brand-block">
      <h2 class="brand"><span class="brand__dot"></span>ZESTMUNCHY</h2>
      <p class="tagline">FRESH ZEST FOOD VAN</p>
    </div>
  </section>

</main>
</body>
</html>
```